IT CEO and Real Estate Investor

It should include two roles and be a two sided card (both roles can be one a single side with a creative view or on different sides).
Card must be creative and interesting, but still professional.
Phone countries(USA/Russia) might be as flags or words, whatever works better.
Boris Melnovetz
Skype: boris_m
E-mail: melnovetz@quorbamail.com
Facebook: plavbook.example/melnovetz
Linkedin: trelnet.example/in/melnovetz
Phone (US): 1(555)316-2947
Phone (RUS): 7(955)482-3170
First role:
Pex Lattor (pexlattor.example) - include logo or part of logo (the $)
E-Commerce Automation Solutions
Founder/CEO/CTO
Second role:
Real Estate Investor
Cleveland, OH
UPDATE:
Let's do one side as logo only and all information on the other side - I don't like designs with information on both sides.
I also really liked designs on black (or other dark) background

```html
<!DOCTYPE html>
<html lang="en">
<head>
<meta charset="UTF-8">
<title>Boris Melnovetz — Business Card</title>
<link rel="stylesheet" href="https://fonts.googleapis.com/css2?family=Roboto:wght@400;500;700&display=swap">
<style>
  :root {
    --page: #2a2d33;
    --card: #1a1a1b;
    --white: #f2f2f2;
    --grey: #9a9a9a;
    --blue: #2aa6df;
    --emboss: #5a5a5c;
    --icon-chat: #2aa0d6;
    --icon-social: #3b66b0;
    --icon-network: #1f7fb8;
    --icon-phone: #7cc242;
  }
  * { margin: 0; padding: 0; box-sizing: border-box; }
  html, body { width: 1200px; height: 900px; overflow: hidden; }
  body {
    background: var(--page);
    font-family: "Roboto", Arial, sans-serif;
    display: flex; flex-direction: column; align-items: center; justify-content: center;
    gap: 40px;
  }
  .card {
    position: relative;
    width: 700px; height: 400px;
    background: var(--card);
    box-shadow: 0 10px 30px rgba(0,0,0,.45);
  }
  /* Front */
  .holder-name {
    position: absolute; left: 44px; top: 42px;
    font-size: 28px; font-weight: 500; letter-spacing: .5px;
    color: var(--white); text-transform: uppercase;
  }
  .holder-name .surname { color: var(--blue); }
  .roles { position: absolute; left: 44px; top: 185px; font-size: 15px; line-height: 1.35; }
  .role-title { color: var(--white); font-weight: 700; }
  .role-detail { color: var(--grey); }
  .role + .role { margin-top: 10px; }
  .front-mark {
    position: absolute; right: 56px; top: 130px;
    display: flex; align-items: center; gap: 12px;
    font-size: 30px; font-weight: 700; color: var(--white);
  }
  .front-mark .mark-square { width: 26px; height: 26px; background: var(--white); }
  .contacts {
    position: absolute; right: 56px; bottom: 36px;
    list-style: none; font-size: 16px; color: var(--grey);
  }
  .contacts li { display: flex; align-items: center; gap: 12px; height: 28px; }
  .contact-dot { width: 20px; height: 20px; border-radius: 50%; flex: none; }
  .dot-chat { background: var(--icon-chat); }
  .dot-social { background: var(--icon-social); }
  .dot-network { background: var(--icon-network); }
  .dot-phone { background: var(--icon-phone); display: flex; align-items: center; justify-content: center; }
  .phone-line .spacer { width: 20px; flex: none; }
  .flag { width: 30px; height: 20px; flex: none; }
  /* Back */
  .back-mark {
    position: absolute; inset: 0;
    display: flex; align-items: center; justify-content: center; gap: 18px;
    font-size: 44px; font-weight: 400; letter-spacing: 8px; color: var(--emboss);
  }
  .back-mark .mark-square { width: 40px; height: 40px; background: var(--emboss); }
</style>
</head>
<body>

<section class="card card-front">
  <h1 class="holder-name">Boris <span class="surname">Melnovetz</span></h1>

  <div class="roles">
    <div class="role">
      <div class="role-title">Real Estate Investor</div>
      <div class="role-detail">Cleveland,OH.</div>
    </div>
    <div class="role">
      <div class="role-title">Founder/CEO/CTO</div>
      <div class="role-detail">Pex Lattor(pexlattor.example)</div>
      <div class="role-detail">E-Commerce Automation Solutions.</div>
    </div>
  </div>

  <div class="front-mark"><span class="mark-square"></span>Pex Lattor</div>

  <ul class="contacts">
    <li><span class="contact-dot dot-chat"></span>boris_m</li>
    <li><span class="contact-dot dot-social"></span>plavbook.example/melnovetz</li>
    <li><span class="contact-dot dot-network"></span>trelnet.example/in/melnovetz</li>
    <li>
      <span class="contact-dot dot-phone">
        <svg width="12" height="12" viewBox="0 0 24 24" aria-hidden="true">
          <path fill="#fff" d="M6.6 10.8a15 15 0 0 0 6.6 6.6l2.2-2.2a1 1 0 0 1 1-.25 11.4 11.4 0 0 0 3.6.57 1 1 0 0 1 1 1V20a1 1 0 0 1-1 1A17 17 0 0 1 3 4a1 1 0 0 1 1-1h3.5a1 1 0 0 1 1 1c0 1.25.2 2.45.57 3.57a1 1 0 0 1-.25 1z"/>
        </svg>
      </span>
      1(555)316-2947
      <svg class="flag" viewBox="0 0 30 20" role="img" aria-label="United States">
        <rect width="30" height="20" fill="#fff"/>
        <g fill="#c8202f">
          <rect y="0" width="30" height="2"/><rect y="4" width="30" height="2"/>
          <rect y="8" width="30" height="2"/><rect y="12" width="30" height="2"/>
          <rect y="16" width="30" height="2"/>
        </g>
        <rect width="13" height="10" fill="#2b3a8c"/>
      </svg>
    </li>
    <li class="phone-line">
      <span class="spacer"></span>
      7(955)482-3170
      <svg class="flag" viewBox="0 0 30 20" role="img" aria-label="Russia">
        <rect width="30" height="7" fill="#fff"/>
        <rect y="7" width="30" height="6" fill="#1c3fa8"/>
        <rect y="13" width="30" height="7" fill="#d52b1e"/>
      </svg>
    </li>
  </ul>
</section>

<section class="card card-back">
  <div class="back-mark"><span class="mark-square"></span>PEX LATTOR</div>
</section>

</body>
</html>
```